Halvern Properties Business Cards

I would like a business card that includes myself and my partner.
Includes: Logo, office #, email, website, our names, our numbers and possibly the address. I would also like the logo to be embossed and the card to be horizontal.
There is a photo of our yard signs to give you an idea of the colors of our business.

Target Market(s)

Everyone in real estate market.
We are in a rural area. Our clientele are from all socioeconomic backgrounds.

Industry/Entity Type

Real Estate Agent

Contact Information for Business Card

Company Name: Halvern Properties
Our Names, Titles & Cell #'s : Marla Halvern-Broker (555).316.4827, Tessa Halvern-Realtor (555).627.9154
Office #: (555).841.2600
Website: halvernproperties-example.com
Joint Email: halvern@halvernproperties-example.com
Office Address: 518B W. Cottonwell Ave.
Cedar Hollow, KS. 70999

Font styles to use
Serif

Requirements
Must have
• HORIZONTAL, Logo, Myself and my partners names, Our cell #'s, our office #, our website, our email address
Nice to have
• Embossed logo, office address, our titles.

```html
<!DOCTYPE html>
<html lang="en">
<head>
<meta charset="utf-8">
<title>Halvern Properties Business Cards</title>
<link rel="stylesheet" href="https://fonts.googleapis.com/css2?family=Noto+Serif:wght@400;700&family=Open+Sans:wght@400&display=swap">
<style>
  :root {
    --backdrop: #e9e6e1;
    --paper: #f4f4f3;
    --ink: #1c1a1f;
    --brand: #4b2b6e;
    --brand-soft: #5e3f84;
    --card-purple: #5a3b7e;
    --emboss: #231830;
  }
  * { box-sizing: border-box; margin: 0; padding: 0; }
  html, body { width: 1200px; height: 443px; overflow: hidden; }
  body { background: var(--backdrop); position: relative; font-family: "Open Sans", sans-serif; color: var(--ink); }

  .card { position: absolute; top: 86px; width: 480px; height: 273px; border-radius: 16px; }
  .card--front { left: 98px; background: var(--paper); }
  .card--back { left: 624px; background: var(--card-purple); display: flex; align-items: center; justify-content: center; }

  .brand { position: absolute; left: 24px; top: 54px; display: flex; align-items: center; gap: 8px; }
  .brand__mark { width: 22px; height: 22px; border-radius: 50%; background: var(--brand); }
  .brand__name { font-family: "Noto Serif", serif; font-weight: 700; font-size: 18px; color: var(--brand); }

  .person { position: absolute; left: 297px; padding-left: 10px; border-left: 5px solid var(--brand); }
  .person--realtor { top: 27px; }
  .person--broker { top: 180px; }
  .person__name { font-family: "Noto Serif", serif; font-size: 20px; line-height: 26px; color: var(--ink); }
  .person__title { font-family: "Noto Serif", serif; font-size: 12.5px; line-height: 16px; color: var(--brand-soft); }
  .person__phone { display: flex; align-items: center; gap: 6px; font-size: 11.5px; line-height: 22px; }

  .contact { position: absolute; left: 30px; top: 0; list-style: none; }
  .contact__item { position: absolute; left: 0; display: flex; align-items: flex-start; gap: 12px; font-size: 11.2px; line-height: 16px; white-space: nowrap; }
  .contact__item svg { flex: none; margin-top: 2px; }
  .contact__item--phone { top: 130px; }
  .contact__item--web { top: 159px; }
  .contact__item--email { top: 178px; }
  .contact__item--address { top: 210px; }

  .icon { width: 12px; height: 12px; fill: var(--brand); }

  .brand-emboss { font-family: "Noto Serif", serif; font-weight: 700; font-size: 34px; color: var(--emboss); letter-spacing: 0.5px; }
</style>
</head>
<body>
  <section class="card card--front" aria-label="Card front">
    <div class="brand">
      <span class="brand__mark"></span>
      <span class="brand__name">Halvern Properties</span>
    </div>

    <div class="person person--realtor">
      <p class="person__name">Tessa Halvern</p>
      <p class="person__title">Realtor</p>
      <p class="person__phone">
        <svg class="icon" viewBox="0 0 12 12"><path d="M3 0h6a1 1 0 0 1 1 1v10a1 1 0 0 1-1 1H3a1 1 0 0 1-1-1V1a1 1 0 0 1 1-1zm0 1.5v8h6v-8zm3 8.6a.6.6 0 1 0 0 1.2.6.6 0 0 0 0-1.2z"/></svg>
        (555).627.9154
      </p>
    </div>

    <div class="person person--broker">
      <p class="person__name">Marla Halvern</p>
      <p class="person__title">Broker</p>
      <p class="person__phone">
        <svg class="icon" viewBox="0 0 12 12"><path d="M3 0h6a1 1 0 0 1 1 1v10a1 1 0 0 1-1 1H3a1 1 0 0 1-1-1V1a1 1 0 0 1 1-1zm0 1.5v8h6v-8zm3 8.6a.6.6 0 1 0 0 1.2.6.6 0 0 0 0-1.2z"/></svg>
        (555).316.4827
      </p>
    </div>

    <ul class="contact">
      <li class="contact__item contact__item--phone">
        <svg class="icon" viewBox="0 0 12 12"><path d="M1 3.5C1 2 3 1.5 6 1.5s5 .5 5 2v1H8.5V3.8h-5v.7H1zM3 5.5h6l1.5 4.5h-9z"/></svg>
        (555).841.2600
      </li>
      <li class="contact__item contact__item--web">
        <svg class="icon" viewBox="0 0 12 12"><path d="M6 .5a5.5 5.5 0 1 0 0 11A5.5 5.5 0 0 0 6 .5zm0 1c.7 0 1.4 1.4 1.6 3.5H4.4C4.6 2.9 5.3 1.5 6 1.5zM1.6 5h1.8c0 .7 0 1.3.1 2H1.6a4.5 4.5 0 0 1 0-2zm2.8 0h3.2v2H4.4zm4.2 0h1.8a4.5 4.5 0 0 1 0 2H8.5c.1-.7.1-1.3.1-2zM4.4 8h3.2c-.2 1.5-.9 2.5-1.6 2.5S4.6 9.5 4.4 8z"/></svg>
        halvernproperties-example.com
      </li>
      <li class="contact__item contact__item--email">
        <svg class="icon" viewBox="0 0 12 12"><path d="M1 2.5h10v.8L6 6.5 1 3.3zm0 2L6 7.7l5-3.2v5H1z"/></svg>
        halvern@halvernproperties-example.com
      </li>
      <li class="contact__item contact__item--address">
        <svg class="icon" viewBox="0 0 12 12"><path d="M6 0a4 4 0 0 0-4 4c0 3 4 8 4 8s4-5 4-8a4 4 0 0 0-4-4zm0 2.4a1.6 1.6 0 1 1 0 3.2 1.6 1.6 0 0 1 0-3.2z"/></svg>
        <span>518B W. Cottonwell Ave.<br>Cedar Hollow, KS. 70999</span>
      </li>
    </ul>
  </section>

  <section class="card card--back" aria-label="Card back">
    <span class="brand-emboss">Halvern Properties</span>
  </section>
</body>
</html>
```